GRHLM 2026 Theme for Wall Banners

We need a design created for a wall banner 4 x 4 feet, for our church's 2026 Theme:
"Applying God's Word"
"Acquiring God's Wisdom"
"Acknowledging God's Will"
"Advancing God's Work"
Proverbs 3:5-6

Use the church's colors purple, silver, white and include the logo
Church Name: Grace-Rooted Harvest Church of Lake Meridian

Target Market(s)

Male & Female, ages 0-99

Industry/Entity Type

Religious, church

Colors
6B429C
8869AF
B7A5CE
E3DAEB
F3F0F8

Requirements
Must have
• Logo, colors, use of all 4 phrases; use of scripture text
Nice to have
• Maybe the phrases in / on pillars
Should not have
• Images or language that is non-Christian

```html
<!DOCTYPE html>
<html lang="en">
<head>
<meta charset="utf-8">
<title>GRHLM 2026 Theme Wall Banner</title>
<link rel="stylesheet" href="https://fonts.googleapis.com/css2?family=Cinzel:wght@600;700&display=swap">
<style>
  :root {
    --stage: #4b4a4c;
    --purple: #6c5190;
    --lilac: #b7a5ce;
    --lilac-soft: #e3daeb;
    --white: #ffffff;
    --deep: #6b429c;
  }
  * { margin: 0; padding: 0; box-sizing: border-box; }
  html, body { width: 1194px; height: 1200px; overflow: hidden; background: var(--stage); }
  body { position: relative; font-family: "Cinzel", "Times New Roman", serif; }

  .banner { position: absolute; left: 147px; top: 145px; width: 899px; height: 895px; }
  .banner__field { position: absolute; left: 0; top: 0; width: 899px; height: 618px; background: var(--purple); }
  .banner__footer { position: absolute; left: 0; top: 618px; width: 899px; height: 277px; background: var(--white); }

  .frame { position: absolute; left: 0; top: 0; width: 899px; height: 618px; pointer-events: none; }

  .theme { position: absolute; width: 380px; text-align: center; color: var(--white); white-space: nowrap; }
  .theme__verb { font-size: 24px; font-weight: 700; line-height: 1; letter-spacing: 0.3px; }
  .theme__object { font-size: 43px; font-weight: 700; line-height: 1; margin-top: 11px; letter-spacing: 0; }

  .theme--word    { left: 52px;  top: 51px; }
  .theme--wisdom  { left: 440px; top: 51px; }
  .theme--will    { left: 52px;  top: 294px; }
  .theme--work    { left: 440px; top: 294px; }

  .pillar { position: absolute; width: 146px; height: 95px; background: rgba(183,165,206,0.35); border-radius: 40px 40px 4px 4px; }
  .pillar--word   { left: 169px; top: 147px; }
  .pillar--wisdom { left: 557px; top: 147px; }
  .pillar--will   { left: 169px; top: 389px; }
  .pillar--work   { left: 557px; top: 389px; }

  .scripture { position: absolute; left: 260px; top: 527px; width: 380px; text-align: center; color: var(--white); font-size: 42px; font-weight: 700; line-height: 1; letter-spacing: 0.5px; white-space: nowrap; }

  .sprig { position: absolute; background: radial-gradient(circle at 50% 55%, var(--lilac) 0%, var(--lilac-soft) 70%, var(--white) 100%); border-radius: 50%; opacity: 0.75; }
  .sprig--left  { left: 38px;  top: 43px; width: 234px; height: 189px; }
  .sprig--right { left: 635px; top: 43px; width: 235px; height: 189px; }

  .church-name { position: absolute; left: 271px; top: 28px; width: 351px; height: 216px; display: flex; flex-direction: column; align-items: center; justify-content: center; gap: 14px; text-align: center; color: var(--deep); font-size: 19px; font-weight: 700; line-height: 1.3; white-space: nowrap; }
  .church-name__dot { width: 22px; height: 22px; border-radius: 50%; background: var(--deep); }
</style>
</head>
<body>
  <main class="banner">
    <section class="banner__field">
      <svg class="frame" viewBox="0 0 899 618" aria-hidden="true">
        <polyline points="91,102 77,102 77,547 260,547" fill="none" stroke="#ffffff" stroke-width="3"/>
        <polyline points="807,102 821,102 821,547 638,547" fill="none" stroke="#ffffff" stroke-width="3"/>
      </svg>

      <div class="theme theme--word"><p class="theme__verb">Applying</p><p class="theme__object">God's Word</p></div>
      <div class="pillar pillar--word" role="img" aria-label="Line drawing of a classical column capital"></div>

      <div class="theme theme--wisdom"><p class="theme__verb">Acquiring</p><p class="theme__object">God's Wisdom</p></div>
      <div class="pillar pillar--wisdom" role="img" aria-label="Line drawing of a classical column capital"></div>

      <div class="theme theme--will"><p class="theme__verb">Acknowledging</p><p class="theme__object">God's Will</p></div>
      <div class="pillar pillar--will" role="img" aria-label="Line drawing of a classical column capital"></div>

      <div class="theme theme--work"><p class="theme__verb">Advancing</p><p class="theme__object">God's Work</p></div>
      <div class="pillar pillar--work" role="img" aria-label="Line drawing of a classical column capital"></div>

      <p class="scripture">Proverbs 3:5-6</p>
    </section>

    <section class="banner__footer">
      <div class="sprig sprig--left" role="img" aria-label="Lilac berry sprig ornament"></div>
      <div class="church-name">
        <span class="church-name__dot" aria-hidden="true"></span>
        <p>Grace-Rooted Harvest Church<br>of Lake Meridian</p>
      </div>
      <div class="sprig sprig--right" role="img" aria-label="Lilac berry sprig ornament"></div>
    </section>
  </main>
</body>
</html>
```